Logistics and freight company requires website

Hi, a Swiftline Cargo company which is based in the United States needs an industry standard website for its activities. We are into forwarding and courier goods from within United States and Canada. We deliver a wide range of goods from shipping of electronics to document, clothings, etc. The proposed website should be comtemporary and youthful. I require brilliant colors for the website. The website should be the basic things of a site. There should a category for shipping electronics, clothings, documents and others( stuffs not listed within the three I mentioned).

```html
<!DOCTYPE html>
<html lang="en">
<head>
<meta charset="utf-8">
<title>Swiftline Cargo</title>
<link href="https://fonts.googleapis.com/css2?family=Montserrat:wght@500;600;700&family=Roboto:wght@400;500&display=swap" rel="stylesheet">
<style>
:root{
  --red:#f63c2a;
  --dark:#2b2b2b;
  --black:#0c0c0c;
  --grey:#f3f3f3;
  --text:#6a6a6a;
  --head:#2a2a2a;
  --white:#fff;
}
*{margin:0;padding:0;box-sizing:border-box}
html,body{width:1200px;height:2250px;overflow:hidden}
body{position:relative;background:var(--white);font-family:'Roboto',sans-serif;color:var(--text)}
.abs{position:absolute}
.mont{font-family:'Montserrat',sans-serif}

/* top bar */
.topbar{left:0;top:0;width:1200px;height:34px}
.toplinks{left:497px;top:11px;font:500 8px 'Montserrat',sans-serif;color:#ddd;display:flex;gap:0}
.toplinks span{padding:0 13px;border-right:1px solid #666}
.toplinks span:last-child{border:none}
.social-dots{left:907px;top:11px;display:flex;gap:20px}
.social-dots i{width:10px;height:10px;border-radius:50%;background:#8a8a8a;display:block}

/* header */
.brand{left:161px;top:37px;display:flex;align-items:center;gap:8px}
.brand-mark{width:26px;height:26px;border-radius:50%;border:3px solid #555}
.brand-name{font:700 17px 'Montserrat',sans-serif;color:var(--red)}
.brand-tag{font-size:10px;color:#777;margin-top:2px}
.infos{left:600px;top:56px;display:flex}
.info{display:flex;gap:8px;padding:0 14px;border-left:1px solid #e2e2e2}
.info-ico{width:9px;height:9px;border:1.5px solid var(--red);border-radius:50%;margin-top:3px}
.info small{display:block;font:500 7.5px 'Montserrat',sans-serif;color:#888}
.info b{font:500 8.5px 'Roboto',sans-serif;color:#333}
.cart{left:984px;top:55px;width:28px;height:28px;border:1px solid #ddd}
.search{left:1012px;top:55px;width:27px;height:28px;background:var(--red)}

/* nav */
.nav{left:0;top:104px}
.navlinks{left:163px;top:123px;display:flex;font:700 9.5px 'Montserrat',sans-serif;color:#fff}
.navlinks span{padding:0 23px;border-right:1px solid rgba(255,255,255,.5)}
.navlinks span:first-child{padding-left:0}

/* hero */
.hero{left:0;top:153px;width:1200px;height:436px;background:linear-gradient(100deg,#c98a4c 0%,#7a6a5d 30%,#4b4e56 55%,#9aa3ad 75%,#5b6069 100%)}
.arrows{left:161px;top:276px;display:flex;gap:4px}
.arrows i{width:30px;height:40px;border:1px solid var(--red);display:block}
.hero-title{left:239px;top:275px;font:700 19px/23px 'Montserrat',sans-serif;color:var(--red)}
.hero-text{left:161px;top:343px;width:420px;font-size:10.5px;line-height:16px;color:var(--red)}
.btn-red{background:var(--red);color:#fff;font:700 9px 'Montserrat',sans-serif;display:flex;align-items:center;justify-content:center;border-right:4px solid #ff7a6c}
.hero-btn{left:161px;top:397px;width:105px;height:32px}

/* welcome */
.welcome-title{left:161px;top:638px;font:700 18px/22px 'Montserrat',sans-serif;color:var(--head)}
.welcome p{font-size:9.6px;line-height:16.5px;width:340px;margin-bottom:16px}
.welcome{left:161px;top:701px}
.btn-outline{border:1px solid #e2e2e2;border-right:3px solid var(--red);font-size:8.5px;color:#888;display:flex;align-items:center;justify-content:center}

/* quote */
.quote{left:536px;top:570px;width:503px;height:368px;background:var(--grey);border-bottom:2px solid #e4e4e4}
.quote h2{position:absolute;left:41px;top:37px;font:700 16px 'Montserrat',sans-serif;color:var(--red)}
.quote h3{position:absolute;left:41px;top:64px;font:400 10px 'Roboto',sans-serif;letter-spacing:2.5px;color:#444}
.field{position:absolute;width:203px;height:34px;background:#fff;font-size:8px;color:#777;padding:12px 14px}

/* modes band */
.modes{left:0;top:973px}
.modes-note{left:804px;top:983px;font:500 11.5px/17px 'Montserrat',sans-serif;color:var(--red)}
.modes-title{left:92px;top:1073px;font:700 19px/24px 'Montserrat',sans-serif;color:#fff}
.modes-text{left:92px;top:1158px;width:266px;text-align:right;font:500 11.5px/17px 'Montserrat',sans-serif;color:#fff}
.mode{width:130px;text-align:center}
.mode-art{width:96px;height:76px;margin:0 auto 10px;background:rgba(0,0,0,.75);border-radius:6px}
.mode b{font:700 19px 'Montserrat',sans-serif;color:#fff}

/* categories */
.cat{width:277px;top:1327px}
.cat-icon{width:143px;height:143px;margin:0 auto;background:var(--red);border:3px solid var(--dark);border-radius:4px;display:flex;align-items:center;justify-content:center}
.cat-card{margin-top:22px;background:var(--grey);height:110px;padding:16px 9px 0;text-align:center}
.cat-card h4{font:600 11px 'Montserrat',sans-serif;color:var(--head);margin-bottom:12px}
.cat-card p{font-size:9.6px;line-height:16.5px;text-align:left}
.cat .btn-outline{width:86px;height:28px;margin-top:11px}

/* cta */
.cta{left:85px;top:1707px;width:1028px;height:87px;background:var(--black)}
.cta h5{position:absolute;left:180px;top:34px;font:700 12.5px 'Montserrat',sans-serif;color:#fff}
.cta p{position:absolute;left:180px;top:54px;font-size:10.5px;color:#fff}
.cta .btn-red{position:absolute;left:650px;top:17px;width:224px;height:51px;font-size:11.5px;border:none}

/* footer */
.footer{left:0;top:1872px}
.f-brand{left:163px;top:1933px}
.f-text{left:164px;top:1988px;width:215px;font-size:9.6px;line-height:16.5px;color:#fff}
.f-social{left:165px;top:2055px;display:flex;gap:7px}
.f-social i{width:15px;height:15px;border:1.5px solid #fff;border-radius:3px;display:block}
.f-btn{left:163px;top:2103px;width:127px;height:31px;border:1px solid #fff;border-right:4px solid #fff;color:#fff;font:700 9px 'Montserrat',sans-serif;display:flex;align-items:center;justify-content:center}
.f-col h6{font:700 11px 'Montserrat',sans-serif;color:#fff;margin-bottom:22px}
.f-col li{list-style:none;font-size:9.6px;color:#ddd;margin-bottom:10px}
.f-contact{left:763px;top:1935px;width:260px;font-size:9.6px;color:#ddd;line-height:16px}
.f-contact h6{font:700 11px 'Montserrat',sans-serif;color:#fff;margin-bottom:18px}
.f-row{display:flex;gap:11px;margin-top:10px}
.f-row i{width:9px;height:9px;background:#ddd;border-radius:2px;margin-top:4px;flex:none}
.copy{left:738px;top:2219px;font-size:9.6px;color:#ccc}
.copy em{font-style:normal;color:var(--red)}
</style>
</head>
<body>

<!-- top bar -->
<svg class="abs topbar" width="1200" height="34" aria-hidden="true">
  <polygon points="450,4 1200,4 1200,34 472,34" fill="#333"/>
  <rect x="0" y="0" width="1200" height="4" fill="#333"/>
</svg>
<div class="abs toplinks"><span>BUY NOW</span><span>READ DOCUMENTATION</span><span>WHY US</span></div>
<div class="abs social-dots"><i></i><i></i><i></i><i></i><i></i></div>

<!-- header -->
<div class="abs brand">
  <div class="brand-mark"></div>
  <div><div class="brand-name">SWIFTLINE CARGO</div><div class="brand-tag">Well Maintained Logistics Services</div></div>
</div>
<div class="abs infos">
  <div class="info"><div class="info-ico"></div><div><small>CALL US</small><b>1.800.555.0142</b></div></div>
  <div class="info"><div class="info-ico"></div><div><small>EMAIL US</small><b>hello@swiftline-cargo.test</b></div></div>
  <div class="info"><div class="info-ico"></div><div><small>WORK HOURS</small><b>Mon - Sat &nbsp;8.00 : 19.00</b></div></div>
</div>
<div class="abs cart"></div>
<div class="abs search"></div>

<!-- nav -->
<svg class="abs nav" width="1200" height="49" aria-hidden="true"><polygon points="40,0 1200,0 1200,49 16,49" fill="var(--red)"/></svg>
<div class="abs navlinks"><span>HOME</span><span>OUR SERVICES</span><span>ABOUT US</span><span>NEWS</span><span>SHOP</span><span>CONTACT</span></div>

<!-- hero -->
<div class="abs hero" role="img" aria-label="Photo of a white container truck at a port at sunset"></div>
<div class="abs arrows"><i></i><i></i></div>
<div class="abs hero-title">ROAD, AIR OR SEA FREIGHT:<br>WE USE THE FASTEST WAY</div>
<div class="abs hero-text">Nunc accumsan metus quis metus. Sed luctus. Mauris eu enim quisque dignissim neque sudm consectetur dapibus wisi et leo integer varius erat.</div>
<div class="abs btn-red hero-btn">LEARN MORE</div>

<!-- welcome -->
<div class="abs welcome-title">WELCOME TO<br>SWIFTLINE CARGO COMPANY</div>
<div class="abs welcome">
  <p>Integer congue elit non semper laoreet sed lectus orcil posuer nisl tempor sed felis acm Pelentesque inyd urna. Integer vitae felis vel magna posu vestibulum. Nam rutrumc diam. Aliquam malesuada maurs etulga metu Curabitur laoreet convallis nisal.</p>
  <p>Pellentesque bibendum. Cras porttitor. Don cursus ante et vulputate feugiat mil justo faucibusn sd Integad elemen tuma volutpat vestibulum enim mi tincidunt. Lorem ipsum dolor sit amet, consectetur adipisicing elit sed do eiusmod tempor incidanaut labore et dolore magna aliqua.</p>
  <div class="btn-outline" style="width:85px;height:28px;margin-top:22px">READ MORE</div>
</div>

<!-- quote form -->
<div class="abs quote">
  <h2>GET A FREE QUOTE</h2>
  <h3>WE ALWAYS USE BEST &amp; FASTEST FLEETS</h3>
  <div class="field" style="left:41px;top:106px">FULL NAME</div>
  <div class="field" style="left:259px;top:106px">EMAIL ADDRESS</div>
  <div class="field" style="left:41px;top:151px">DESTINATION FROM</div>
  <div class="field" style="left:259px;top:151px">DESTINATION TO</div>
  <div class="field" style="left:41px;top:196px">SUBJECT</div>
  <div class="field" style="left:259px;top:196px;height:79px">COMMENTS</div>
  <div class="field" style="left:41px;top:241px">PHONE NO.</div>
  <div class="btn-red" style="position:absolute;left:259px;top:292px;width:203px;height:35px">SEND ME QUOTE</div>
</div>

<!-- modes band -->
<svg class="abs modes" width="1200" height="280" aria-hidden="true">
  <rect width="1200" height="280" fill="var(--grey)"/>
  <polygon points="0,0 0,0 1200,84 1200,279 0,279" fill="var(--red)"/>
</svg>
<div class="abs modes-note">We are into forwarding and courier goods<br>from within United States and Canada.</div>
<div class="abs modes-title">ROAD, AIR OR SEA FREIGHT:<br>WE USE THE FASTEST WAY</div>
<div class="abs modes-text">We have wide network of offices in all major locations to help you with the services we offer Recomended Logistics and freight company</div>
<div class="abs mode" style="left:439px;top:1075px"><div class="mode-art" role="img" aria-label="Delivery truck icon"></div><b>ROAD</b></div>
<div class="abs mode" style="left:657px;top:1075px"><div class="mode-art" role="img" aria-label="Cargo ship icon"></div><b>SEA</b></div>
<div class="abs mode" style="left:906px;top:1075px"><div class="mode-art" role="img" aria-label="Airplane icon"></div><b>AIR</b></div>

<!-- categories -->
<div class="abs cat" style="left:161px">
  <div class="cat-icon">
    <svg width="110" height="100" viewBox="0 0 110 100" aria-hidden="true"><polygon points="55,8 104,92 6,92" fill="#fff" stroke="var(--dark)" stroke-width="7" stroke-linejoin="round"/></svg>
  </div>
  <div class="cat-card"><h4>ELECTRONICS</h4><p>Integer congue, elit non semper laoreet sed lectus orci posuh nisl tempor lacus felis ac mauris. Pellentesque in urna. Intege vitae felis vel magna posuere vestibulum.</p></div>
  <div class="btn-outline">READ MORE</div>
</div>
<div class="abs cat" style="left:461px">
  <div class="cat-icon">
    <svg width="120" height="110" viewBox="0 0 120 110" aria-hidden="true"><path d="M40,8 Q60,24 80,8 L116,40 98,58 88,48 88,104 32,104 32,48 22,58 4,40 Z" fill="#fff" stroke="var(--dark)" stroke-width="6" stroke-linejoin="round"/></svg>
  </div>
  <div class="cat-card"><h4>CLOTHINGS</h4><p>Integer congue, elit non semper laoreet sed lectus orci posuh nisl tempor lacus felis ac mauris. Pellentesque in urna. Intege vitae felis vel magna posuere vestibulum.</p></div>
  <div class="btn-outline">READ MORE</div>
</div>
<div class="abs cat" style="left:761px">
  <div class="cat-icon">
    <svg width="90" height="115" viewBox="0 0 90 115" aria-hidden="true">
      <path d="M8,6 L60,6 84,30 84,108 8,108 Z" fill="#fff" stroke="var(--dark)" stroke-width="6" stroke-linejoin="round"/>
      <path d="M60,6 L60,30 84,30" fill="none" stroke="var(--dark)" stroke-width="6"/>
      <path d="M24,58 H68 M24,74 H68 M24,90 H68" stroke="var(--dark)" stroke-width="6"/>
    </svg>
  </div>
  <div class="cat-card"><h4>DOCUMENTS AND OTHERS</h4><p>Integer congue, elit non semper laoreet sed lectus orci posuh nisl tempor lacus felis ac mauris. Pellentesque in urna. Intege vitae felis vel magna posuere vestibulum.</p></div>
  <div class="btn-outline">READ MORE</div>
</div>

<!-- call to action -->
<div class="abs cta">
  <h5>WE PROVIDE FASTEST &amp; AFFORDABLE CARGO SERVICES</h5>
  <p>Lorem ipsum dolor sit amet, consectetur adipisicing elit, sed do eiusmod tempor incididunt</p>
  <div class="btn-red">REQUEST A FREE QUOTE</div>
</div>

<!-- footer -->
<svg class="abs footer" width="1200" height="378" aria-hidden="true">
  <rect width="1200" height="378" fill="var(--dark)"/>
  <polygon points="0,0 440,0 362,323 0,323" fill="var(--red)"/>
  <rect y="323" width="1200" height="55" fill="var(--black)"/>
  <polygon points="124,323 187,323 164,378 102,378" fill="#3a3a3a"/>
  <path d="M139,354 L145,348 151,354" fill="none" stroke="#fff" stroke-width="1.5"/>
</svg>
<div class="abs f-brand brand" style="left:163px;top:1933px">
  <div class="brand-mark" style="border-color:#fff"></div>
  <div><div class="brand-name" style="color:var(--dark)">SWIFTLINE CARGO</div><div class="brand-tag" style="color:#fff">Well Maintained Logistics Services</div></div>
</div>
<div class="abs f-text">Integer congue elit non semper laoreet sed lectu orc posuer nisl tempor sed felis ac mauris ellent esque ndu ca uma Integer vitae felis.</div>
<div class="abs f-social"><i></i><i></i><i></i><i></i><i></i></div>
<div class="abs f-btn">GET A FREE QUOTE</div>

<div class="abs f-col" style="left:463px;top:1935px">
  <h6>WE OFFERS</h6>
  <ul><li>Sea Freight</li><li>Road Transportation</li><li>Air Freight</li><li>Railway Logistics</li><li>Packaging &amp; Storage</li><li>Warehousing</li></ul>
</div>
<div class="abs f-col" style="left:613px;top:1935px">
  <h6>MAIN LINKS</h6>
  <ul><li>Home</li><li>Our Services</li><li>About Us</li><li>News</li><li>Shop</li><li>Contact</li></ul>
</div>
<div class="abs f-contact">
  <h6>CONTACT INFO</h6>
  <div>Everyday is a new day for us and we work really hard to satisfy our customers everywhere.</div>
  <div class="f-row" style="margin-top:16px"><i></i><div><b style="color:#fff;font-weight:500">SWIFTLINE CARGO COMPANY.</b><br>1207 Harbor Crest Road, Portview 40218</div></div>
  <div class="f-row"><i></i><div>1.800.555.0142</div></div>
  <div class="f-row" style="margin-top:6px"><i></i><div>hello@swiftline-cargo.test &nbsp;| &nbsp;quotes@swiftline-cargo.test</div></div>
  <div class="f-row" style="margin-top:6px"><i></i><div>Mon - Sat &nbsp;8.00 - 19.00</div></div>
</div>
<div class="abs copy">Created by <em>Swiftline Cargo</em> © 2016 &nbsp;All rights reserved.</div>

</body>
</html>
```